Cover Design

This design is for a workbook that I use with my students. I am looking to refresh the cover design of the book. Attached is what the book cover looks like now and I don't like it. I'd really like to see something more creative, more modern and more inviting.

Need extra days to review

```html
<!DOCTYPE html>
<html lang="en">
<head>
<meta charset="utf-8">
<title>HR Decoded – Workbook Cover</title>
<link rel="stylesheet" href="https://fonts.googleapis.com/css2?family=Bebas+Neue&display=swap">
<style>
  :root {
    --frame: #050505;
    --paper: #ffffff;
    --orange: #ee6437;
    --orange-light: #f59a5c;
    --yellow: #f6b034;
    --ink: #0a0a0a;
  }
  * { margin: 0; padding: 0; box-sizing: border-box; }
  html, body {
    width: 972px; height: 1200px; overflow: hidden;
    background: var(--frame);
  }
  .cover {
    position: relative;
    width: 972px; height: 1200px;
    background: var(--frame);
    font-family: "Bebas Neue", "Oswald", sans-serif;
  }
  .cover-art { position: absolute; inset: 0; display: block; }
  .title, .subtitle, .tagline, .author {
    position: absolute;
    line-height: 1;
    white-space: nowrap;
    font-weight: 400;
  }
  .title {
    left: 110px; top: 172px;
    font-size: 154px;
    letter-spacing: 1px;
    color: var(--paper);
  }
  .subtitle {
    left: 111px; top: 343px;
    font-size: 69px;
    line-height: 61px;
    letter-spacing: 2px;
    color: var(--paper);
  }
  .tagline {
    left: 466px; top: 970px;
    font-size: 29px;
    line-height: 26px;
    letter-spacing: 0.9px;
    color: var(--ink);
  }
  .author {
    left: 465px; top: 1053px;
    font-size: 76px;
    letter-spacing: 3.5px;
    color: var(--ink);
  }
</style>
</head>
<body>
<main class="cover">
  <svg class="cover-art" viewBox="0 0 972 1200" width="972" height="1200">
    <defs>
      <linearGradient id="art-fill" x1="0" y1="0" x2="1" y2="1">
        <stop offset="0" stop-color="var(--orange-light)"/>
        <stop offset="0.6" stop-color="var(--orange)"/>
        <stop offset="1" stop-color="var(--yellow)"/>
      </linearGradient>
    </defs>
    <rect class="panel" x="50" y="62" width="870" height="1087" fill="var(--paper)"/>
    <polygon class="art-area" role="img"
      aria-label="Decorative pattern of diagonal orange stripes with scattered yellow and orange squares"
      points="50,62 920,62 920,481 50,1012" fill="url(#art-fill)"/>
  </svg>

  <h1 class="title">HR DECODED</h1>
  <p class="subtitle">HR CERTIFICATION<br>WORKBOOK</p>
  <p class="tagline">EQUIPPING HR PROS WITH THE TOOLS NEEDED<br>TO ACE THEIR CERTIFICATION EXAMS</p>
  <p class="author">DANA WHITFIELD</p>
</main>
</body>
</html>
```